Law Firm Advertising Design Needed

Law Office of Dorvel K Tansy provides legal services to businesses and individuals who have been or are being injured. Our main practice area is personal injury (car accidents, wrongful death, premises liability), but we are looking for an ad that highlights a lesser known area of our practice - insurance company bad faith and breach of contract.

This ad will be placed in 8 1/2" x 11" format in a local neighborhood directory. It will also be placed in a smaller format (to be determined) in the local newspaper of a region of Arizona that has recently lost a considerable number of homes and people to wildfire.

We want to convey through the ad that our firm is available to help if their insurance company is not paying a legitimate claim or not paying enough for their claim.

Because of the tragic nature of the events in Yarnell, we would like to avoid images of fire or anything resembling fire. However, the ad should capture the attention of individuals who are struggling through an insurance claim with all the stacks of paperwork and frustrated with unresponsive adjusters and unreasonably low offers.

The design should convey a feeling of safety, security and being taken care of.

Information that must be included in the ad are: the firm name (Law Office of Dorvel K Tansy), address (4857 W 17th Avenue, Ste 406, Phoenix, AZ 85033), the phone number (602-574-2930) and the fact that we have mobile offices available to assist in your area.

An example of text that has been used in the past is here:
"If your own insurance company is refusing to pay what you are owed on a claim, call the Law Office of Dorvel K Tansy. We fight for you by examining the reasons your insurance carrier is denying or making an insufficient offer on the claim; updating and correcting claim documentation; making a new demand and filing a lawsuit if necessary. Whether it's a simple misunderstanding or something more complicated, we can help!

Here are a few of the kinds of claims we handle:
- Hit and Run or Uninsured driver claims
- Fire, flood and property loss
- Life insurance benefits
- Health insurance claims
- Catastrophic losses
- Business insurance
- Wrongful Death Benefits

Our attorneys are available to help you cut through the nonsense. Call to make an appointment for a free consultation with an attorney today. "

An example of a previous ad for car accident services is attached for reference.
Updates

Hi Everyone,

The main lawyer involved in the decision making process has been giving me some feedback in general on the designs that I thought I would pass along.  He does not want the name of the law firm to be the first thing you notice when you look at the ad. Try to keep that small and possibly to the bottom of the ad. The phone number should be rather large, but the address should be rather small (we are required by the State Bar to include our address, but we don't want our location to limit the location of our clients because our mobile offices can travel to them).  He would prefer that the logo either not be included or be not a significant part of the ad.

                                   

Thanks!  I will continue providing individual feedback to ads received. 

Target Market(s)

Low to middle income residents of the State of Arizona with little or no college education

Industry/Entity Type

Insurance

```html
<!DOCTYPE html>
<html lang="en">
<head>
<meta charset="utf-8">
<title>Law Office of Dorvel K Tansy – Insurance Claims Ad</title>
<link href="https://fonts.googleapis.com/css2?family=Montserrat:wght@500;600;700&family=Arimo:wght@400;700&display=swap" rel="stylesheet">
<style>
  :root {
    --blue: #2f4ea6;
    --sky: #8ea2d8;
    --paper: #ffffff;
    --ink: #111111;
    --portrait-dark: #2a2320;
    --portrait-light: #7a6a5c;
  }
  * { margin: 0; padding: 0; box-sizing: border-box; }
  html, body { width: 844px; height: 1200px; overflow: hidden; background: var(--paper); }
  .ad {
    position: relative;
    width: 844px; height: 1200px;
    background: linear-gradient(to bottom, var(--sky) 0%, #c3cdec 18%, var(--paper) 34%, var(--paper) 100%);
    color: var(--ink);
    font-family: "Arimo", Arial, sans-serif;
  }
  .headline {
    position: absolute; top: 40px; left: 0; width: 100%;
    text-align: center;
    font-family: "Montserrat", Arial, sans-serif;
    font-weight: 500;
    color: var(--blue);
    font-size: 79px; line-height: 120px; letter-spacing: -0.5px;
  }
  .intro {
    position: absolute; top: 480px; left: 49px; width: 756px;
    font-size: 15px; line-height: 21px; text-align: justify;
  }
  .intro strong {
    font-family: "Montserrat", Arial, sans-serif;
    font-weight: 700; font-size: 19px;
  }
  .claims {
    position: absolute; top: 680px; left: 46px; width: 780px;
    font-family: "Montserrat", Arial, sans-serif;
  }
  .claims h2 { font-size: 22.5px; font-weight: 700; margin-bottom: 2px; white-space: nowrap; }
  .claims ul {
    list-style: none;
    display: grid; grid-template-columns: 442px 338px; grid-auto-flow: column; grid-template-rows: repeat(4, 27px);
    font-size: 19px; font-weight: 500;
  }
  .claims li { position: relative; padding-left: 27px; line-height: 27px; white-space: nowrap; }
  .claims li::before {
    content: ""; position: absolute; left: 3px; top: 8px;
    width: 11px; height: 11px; border: 2px solid var(--ink); transform: rotate(45deg);
  }
  .claims li::after {
    content: ""; position: absolute; left: 7px; top: 12px;
    width: 5px; height: 5px; background: var(--ink); transform: rotate(45deg);
  }
  .closing {
    position: absolute; top: 862px; left: 0; width: 100%;
    text-align: center; font-size: 18px; line-height: 26px;
  }
  .firm-mark {
    position: absolute; top: 994px; left: 46px; width: 156px; height: 167px;
    display: flex; align-items: center; justify-content: center; gap: 10px;
  }
  .firm-mark .square { width: 14px; height: 14px; background: var(--ink); }
  .firm-mark .name { font-family: "Montserrat", Arial, sans-serif; font-weight: 600; font-size: 34px; }
  .contact { position: absolute; top: 1020px; left: 217px; white-space: nowrap; }
  .contact .firm { font-family: "Montserrat", Arial, sans-serif; font-weight: 700; color: var(--blue); font-size: 21.5px; line-height: 28px; }
  .contact .address { font-size: 16.5px; line-height: 22px; }
  .contact .phone { font-family: "Montserrat", Arial, sans-serif; font-weight: 500; font-size: 42px; line-height: 54px; margin-top: 4px; letter-spacing: 0.5px; }
  .portrait {
    position: absolute; top: 1010px; left: 635px; width: 153px; height: 133px;
    background: linear-gradient(135deg, var(--portrait-light) 0%, var(--portrait-dark) 70%);
  }
  .website {
    position: absolute; top: 1150px; left: 612px; width: 200px;
    text-align: center; font-size: 14px; font-weight: 700;
  }
</style>
</head>
<body>
<main class="ad">
  <h1 class="headline">Any Accident,<br>Any Injury...<br>Let us fight for you!</h1>

  <p class="intro"><strong>If your own insurance company is refusing to pay</strong> what you are owed on a claim, call the Law Office of Dorvel K Tansy. We fight for you by examining the reasons your insurance carrier is denying or making an insufficient offer on the claim; updating and correcting claim documentation; making a new demand and filing a lawsuit if necessary. Whether it's a simple misunderstanding or something more complicated, we can help!</p>

  <section class="claims">
    <h2>Here are a few of the kinds of claims we handle :</h2>
    <ul>
      <li>Hit and Run or Uninsured driver claims</li>
      <li>Life insurance benefits</li>
      <li>Catastrophic losses</li>
      <li>Wrongful Death Benefits</li>
      <li>Fire, flood and property loss</li>
      <li>Health insurance claims</li>
      <li>Business insurance</li>
    </ul>
  </section>

  <p class="closing">Our attorneys are available to help you cut through the nonsense.<br>Call to make an appointment for a free consultation with an attorney today.</p>

  <div class="firm-mark"><span class="square"></span><span class="name">Tansy</span></div>

  <div class="contact">
    <p class="firm">Law Office of Dorvel K Tansy</p>
    <p class="address">(4857 W 17th Avenue, Ste 406, Phoenix, AZ 85033</p>
    <p class="phone">(602) 574 2930</p>
  </div>

  <div class="portrait" role="img" aria-label="Portrait photo of the attorney seated at his desk"></div>
  <p class="website">www.tansylawaz.com</p>
</main>
</body>
</html>
```